Business Card Design.

Life and Wellness Coach
www.brightpathwell.net
Want to use my name as the logo it could be the initials TRK or my full name. I want to trade mark me.
I like clean lines and simple designs, but it pops using the colors scheme (one or two colors) on the website.
I provide life and health coaching virtually and in person. My services include: Dietary Signal Screening, Sensitivity Clearing Review, Wellness Coaching, Life Coaching. Life and Health Assessments, and I sell foundational health products and specialized nutrition. Use colors that represent healing and trust.
Target Market(s)
Women for the ages of 30 - 60
Industry/Entity Type
Health
Contact Information for Business Card
Tessa Rosalind Kimble
Life and Wellness Coach
tessa@coachtrk.net
www.brightpathwell.net
555-217-8364
Health is not an event it's a lifestyle (tag line or if you have a better tag line)

```html
<!DOCTYPE html>
<html lang="en">
<head>
<meta charset="utf-8">
<title>Tessa Rosalind Kimble – Business Card</title>
<link rel="stylesheet" href="https://fonts.googleapis.com/css2?family=Fondamento&family=Arimo:wght@400&display=swap">
<style>
  :root{
    --berry:#a3285e;
    --charcoal:#3c3c3e;
    --stage:#e9e6e2;
    --ink-light:#ffffff;
    --photo-tone-a:#7a4a3a;
    --photo-tone-b:#d9b3a0;
    --photo-accent:#2c3f9e;
  }
  *{box-sizing:border-box;margin:0;padding:0}
  html,body{width:1200px;height:848px;overflow:hidden;background:var(--stage)}
  .stage{width:1200px;height:848px;display:flex;flex-direction:column;align-items:center;justify-content:center;gap:30px}
  .card{width:660px;height:377px;border-radius:22px;position:relative;overflow:hidden;box-shadow:0 8px 22px rgba(0,0,0,.22)}
  .card--front{background:linear-gradient(180deg,var(--berry) 0%,var(--charcoal) 100%)}
  .portrait{position:absolute;left:0;top:0;width:290px;height:100%;border-radius:0 26px 26px 0;
    background:radial-gradient(ellipse at 45% 45%,var(--photo-tone-b) 0%,var(--photo-tone-a) 55%,var(--photo-accent) 100%)}
  .identity{position:absolute;left:318px;top:46px;color:var(--ink-light)}
  .identity__name{font-family:"Fondamento",cursive;font-size:28px;letter-spacing:.3px}
  .identity__role{font-family:"Arimo",Arial,sans-serif;font-size:17px;margin-top:2px;opacity:.95}
  .contacts{position:absolute;left:318px;top:238px;list-style:none;font-family:"Arimo",Arial,sans-serif;font-size:17px;color:var(--ink-light)}
  .contacts li{display:flex;align-items:center;gap:12px;height:30px}
  .contacts svg{width:24px;height:24px;flex:none}
  .card--back{background:linear-gradient(150deg,var(--berry) 0%,var(--charcoal) 72%)}
  .tagline{position:absolute;right:40px;bottom:44px;font-family:"Fondamento",cursive;font-size:32px;color:var(--ink-light);text-shadow:0 1px 2px rgba(0,0,0,.35)}
</style>
</head>
<body>
<main class="stage">
  <section class="card card--front">
    <div class="portrait" role="img" aria-label="Portrait photograph of Tessa Rosalind Kimble"></div>
    <header class="identity">
      <h1 class="identity__name">Tessa Rosalind Kimble</h1>
      <p class="identity__role">Life and Wellness Coach</p>
    </header>
    <ul class="contacts">
      <li>
        <svg viewBox="0 0 24 24" aria-hidden="true"><rect width="24" height="24" rx="3" fill="var(--berry)"/><path d="M7 5l3 3-1.6 1.8a10 10 0 0 0 5.8 5.8L16 14l3 3-2 2C10.5 18.5 5.5 13.5 5 7z" fill="#fff"/></svg>
        <span>555-217-8364</span>
      </li>
      <li>
        <svg viewBox="0 0 24 24" aria-hidden="true"><rect width="24" height="24" rx="3" fill="var(--berry)"/><circle cx="12" cy="12" r="6.5" fill="none" stroke="#fff" stroke-width="1.6"/><path d="M5.5 12h13M12 5.5c-3 3.5-3 9.5 0 13M12 5.5c3 3.5 3 9.5 0 13" fill="none" stroke="#fff" stroke-width="1.3"/></svg>
        <span>www.brightpathwell.net</span>
      </li>
      <li>
        <svg viewBox="0 0 24 24" aria-hidden="true"><rect width="24" height="24" rx="3" fill="var(--berry)"/><rect x="5" y="7" width="14" height="10" fill="none" stroke="#fff" stroke-width="1.6"/><path d="M5 7l7 6 7-6" fill="none" stroke="#fff" stroke-width="1.6"/></svg>
        <span>tessa@coachtrk.net</span>
      </li>
    </ul>
  </section>
  <section class="card card--back">
    <p class="tagline">Health is not an event it's a lifestyle</p>
  </section>
</main>
</body>
</html>
```